Need a Basketball Court Design

We are replacing our current basketball court (gym floor) and we are looking for a new design. Our team is the “Harborview Falcons”. Our mascot is a “Knight” (in shining armor). Our colors are royal blue/grey/black. We are looking for a design that is contemporary and energetic.
The background of the court should display a “castle”. In the center of the court should be a team logo. You can use one of our existing logos or create your own. Along the baseline of the court should read the word “Harborview”.
I’ve attached ...
1) a picture of the current court
2) a mock-up design of what we are thinking
3) some of the different team logos we use.

```html
<!DOCTYPE html>
<html lang="en">
<head>
<meta charset="utf-8">
<title>Harborview Falcons Court</title>
<link rel="stylesheet" href="https://fonts.googleapis.com/css2?family=Roboto+Slab:wght@800&display=swap">
<style>
  :root {
    --page: #ffffff;
    --border-black: #050505;
    --line-white: #ffffff;
    --royal-blue: #254c96;
    --wood-light: #e9c48f;
    --wood-mid: #dcae74;
  }
  html, body {
    margin: 0;
    padding: 0;
    width: 1200px;
    height: 600px;
    overflow: hidden;
    background: var(--page);
  }
  .court-design {
    position: relative;
    width: 1200px;
    height: 600px;
  }
  .court-svg {
    position: absolute;
    inset: 0;
  }
  .court-word {
    font-family: "Roboto Slab", serif;
    font-weight: 800;
    fill: var(--line-white);
  }
  .side-word { font-size: 60px; }
  .baseline-word { font-size: 34px; }
  .team-name {
    font-family: "Roboto Slab", serif;
    font-weight: 800;
    fill: var(--border-black);
    font-size: 30px;
    letter-spacing: 2px;
  }
  .corner-name {
    font-family: "Roboto Slab", serif;
    font-weight: 800;
    fill: var(--border-black);
    font-size: 11px;
    letter-spacing: 1px;
  }
</style>
</head>
<body>
<main class="court-design">
  <svg class="court-svg" width="1200" height="600" viewBox="0 0 1200 600" xmlns="http://www.w3.org/2000/svg">
    <defs>
      <linearGradient id="wood-tone" x1="0" y1="0" x2="1" y2="1">
        <stop offset="0" stop-color="var(--wood-light)"/>
        <stop offset="0.5" stop-color="var(--wood-mid)"/>
        <stop offset="1" stop-color="var(--wood-light)"/>
      </linearGradient>
    </defs>

    <rect class="apron" x="67" y="13" width="1077" height="574" fill="var(--border-black)"/>

    <rect class="wood-floor" x="135" y="50" width="938" height="498" fill="url(#wood-tone)" role="img" aria-label="Maple hardwood floor boards"/>

    <g class="court-lines" fill="none" stroke="var(--line-white)" stroke-width="2.5">
      <rect x="135" y="50" width="938" height="498"/>
      <line x1="605" y1="50" x2="605" y2="548"/>
      <path d="M135 102 H195 A192 197 0 0 1 195 497 H135"/>
      <path d="M1073 102 H1013 A192 197 0 0 0 1013 497 H1073"/>
    </g>

    <g class="key key-left">
      <rect x="136" y="238" width="177" height="119" fill="var(--border-black)"/>
      <path d="M313 237 A60 60 0 0 0 313 357 Z" fill="var(--royal-blue)" stroke="var(--line-white)" stroke-width="2"/>
      <path d="M313 237 A62 60 0 0 1 313 357" fill="none" stroke="var(--line-white)" stroke-width="2.5"/>
      <line x1="313" y1="237" x2="313" y2="357" stroke="var(--line-white)" stroke-width="2"/>
      <line x1="165" y1="262" x2="165" y2="333" stroke="var(--line-white)" stroke-width="2.5"/>
      <line x1="165" y1="297" x2="170" y2="297" stroke="var(--line-white)" stroke-width="2.5"/>
      <circle cx="187" cy="297" r="17" fill="none" stroke="var(--line-white)" stroke-width="2.5"/>
      <g stroke="var(--line-white)" stroke-width="2">
        <line x1="200" y1="231" x2="200" y2="238"/><line x1="228" y1="231" x2="228" y2="238"/>
        <line x1="257" y1="231" x2="257" y2="238"/><line x1="286" y1="231" x2="286" y2="238"/>
        <line x1="200" y1="357" x2="200" y2="364"/><line x1="228" y1="357" x2="228" y2="364"/>
        <line x1="257" y1="357" x2="257" y2="364"/><line x1="286" y1="357" x2="286" y2="364"/>
      </g>
    </g>

    <g class="key key-right" transform="translate(1209 0) scale(-1 1)">
      <rect x="136" y="238" width="177" height="119" fill="var(--border-black)"/>
      <path d="M313 237 A60 60 0 0 0 313 357 Z" fill="var(--royal-blue)" stroke="var(--line-white)" stroke-width="2"/>
      <path d="M313 237 A62 60 0 0 1 313 357" fill="none" stroke="var(--line-white)" stroke-width="2.5"/>
      <line x1="313" y1="237" x2="313" y2="357" stroke="var(--line-white)" stroke-width="2"/>
      <line x1="165" y1="262" x2="165" y2="333" stroke="var(--line-white)" stroke-width="2.5"/>
      <line x1="165" y1="297" x2="170" y2="297" stroke="var(--line-white)" stroke-width="2.5"/>
      <circle cx="187" cy="297" r="17" fill="none" stroke="var(--line-white)" stroke-width="2.5"/>
      <g stroke="var(--line-white)" stroke-width="2">
        <line x1="200" y1="231" x2="200" y2="238"/><line x1="228" y1="231" x2="228" y2="238"/>
        <line x1="257" y1="231" x2="257" y2="238"/><line x1="286" y1="231" x2="286" y2="238"/>
        <line x1="200" y1="357" x2="200" y2="364"/><line x1="228" y1="357" x2="228" y2="364"/>
        <line x1="257" y1="357" x2="257" y2="364"/><line x1="286" y1="357" x2="286" y2="364"/>
      </g>
    </g>

    <g class="center-mark">
      <circle cx="605" cy="232" r="34" fill="var(--royal-blue)"/>
      <text class="team-name" x="605" y="316" text-anchor="middle">HARBORVIEW</text>
      <text class="team-name" x="605" y="354" text-anchor="middle">FALCONS</text>
    </g>

    <text class="corner-name" x="207" y="432" text-anchor="middle">HARBORVIEW</text>
    <text class="corner-name" x="1000" y="175" text-anchor="middle">HARBORVIEW</text>

    <text class="court-word side-word" transform="translate(123 292) rotate(-90)" text-anchor="middle" textLength="295" lengthAdjust="spacing">FALCONS</text>
    <text class="court-word side-word" transform="translate(1085 293) rotate(90)" text-anchor="middle" textLength="437" lengthAdjust="spacing">BASKETBALL</text>
    <text class="court-word baseline-word" x="615" y="581" text-anchor="middle" textLength="586" lengthAdjust="spacing">WELCOME TO THE HARBORSIDE</text>
  </svg>
</main>
</body>
</html>
```